Verpackungen für elektronische Entspannungsgeräte
You did a great job!!! Thank you very much and thank you for your patience as well. It was great working with you. Many Greetings from Germany :-))) Tessa
Zielgruppe
Wir stellen elektronische Entspannungsgeräte her. Für Jedermann, jeden Alters.
Aufgabenstellung
Jetzt bäuchte ich für eine Umverpackung ein Design. Außen auf der Verpackung soll das Design drauf und innen auf der Deckelseite soll in schöner Schrift stehen:
'Herzlichen Glückwunsch zu einem entspannteren Leben :-)'
Das Design auf der Verpackung soll viel weiß enthalten. Es soll elegant, aber schlicht gehalten sein, in den gleichen Farben wie das Logo.
Die Umverpackung wird ca. 15 x 10 x 4 cm groß sein. Bitte eine Vektorgrafik, die ich entsprechend vergrößern kann.
CE sollte drauf.
Vorsel GmbH, www.vorsel-gmbh.example; Am Querweg 14, 65491 Ostrach
Ich freue mich auf Vorschläge :-)

```html
<!DOCTYPE html>
<html lang="de">
<head>
<meta charset="utf-8">
<title>Vorsel – Verpackung</title>
<link href="https://fonts.googleapis.com/css2?family=Roboto:wght@300;400;500&family=Montserrat:wght@700&display=swap" rel="stylesheet">
<style>
  :root {
    --canvas: #e3e5e1;
    --paper: #ffffff;
    --ink: #111417;
    --brand: #0d3a5c;
    --line: #5a5f63;
    --teal: #3ee8d6;
    --aqua: #00c9e4;
    --sky: #86bff0;
  }
  html, body {
    margin: 0;
    width: 1200px;
    height: 1200px;
    overflow: hidden;
    background: var(--canvas);
    font-family: "Roboto", Arial, sans-serif;
    color: var(--ink);
  }
  .sheet {
    position: absolute;
    left: 220px;
    width: 760px;
    background: var(--paper);
    box-shadow: 0 4px 8px rgba(0,0,0,0.18);
  }
  .lid { top: 70px; height: 510px; overflow: hidden; }
  .colour-field {
    position: absolute;
    left: 0;
    right: 0;
    top: 350px;
    bottom: 0;
    background: linear-gradient(100deg, var(--aqua) 0%, var(--teal) 50%, var(--sky) 100%);
  }
  .brand-name {
    position: absolute;
    left: 78px;
    top: 62px;
    font-family: "Montserrat", Arial, sans-serif;
    font-weight: 700;
    font-size: 28px;
    color: var(--brand);
    display: flex;
    align-items: center;
    gap: 8px;
  }
  .brand-dot {
    width: 12px; height: 12px; border-radius: 50%;
    background: var(--aqua);
  }
  .claim {
    position: absolute;
    left: 228px;
    top: 212px;
    margin: 0;
    font-weight: inherit;
    line-height: 1;
  }
  .claim-top { display: block; font-weight: 300; font-size: 36px; letter-spacing: 0.5px; }
  .claim-main { display: block; font-weight: 500; font-size: 44px; margin-top: 4px; }

  .side { top: 620px; height: 120px; display: flex; align-items: center; justify-content: center; }
  .imprint {
    display: flex;
    border: 1px solid var(--line);
    height: 44px;
    align-items: stretch;
  }
  .imprint-text {
    padding: 0 26px;
    display: flex; align-items: center;
    font-size: 13px;
    color: var(--ink);
  }
  .mark-cell {
    width: 70px;
    border-left: 1px solid var(--line);
    display: flex; align-items: center; justify-content: center;
  }
  .mark-shape { width: 30px; height: 18px; border: 1.5px solid var(--line); }

  .inside { top: 780px; height: 340px; display: flex; align-items: center; justify-content: center; }
  .greeting {
    border: 1px solid var(--line);
    padding: 16px 44px;
    margin: 0;
    text-align: center;
    font-size: 20px;
    line-height: 1.3;
    color: #3a3f43;
  }
</style>
</head>
<body>
  <section class="sheet lid" aria-label="Deckel">
    <div class="colour-field" role="img" aria-label="Farbfläche in Türkis und Hellblau"></div>
    <div class="brand-name"><span class="brand-dot"></span>Vorsel</div>
    <h1 class="claim">
      <span class="claim-top">MADE TO</span>
      <span class="claim-main">RELAX</span>
    </h1>
  </section>

  <section class="sheet side" aria-label="Seitenfläche">
    <div class="imprint">
      <span class="imprint-text">Vorsel GmbH, www.vorsel-gmbh.example; Am Querweg 14, 65491 Ostrach</span>
      <span class="mark-cell"><span class="mark-shape"></span></span>
    </div>
  </section>

  <section class="sheet inside" aria-label="Deckelinnenseite">
    <p class="greeting">Herzlichen Glückwunsch<br>zu einem entspannteren Leben :)</p>
  </section>
</body>
</html>
```